Bref créative
Stationery
Health centre
Bright & Fun-filled
Meadowlark Wellness Studio
We need cards for different individuals - easily editable
12B Harlow Terrace
Edinburgh
EH4 7QN
info@meadowlarkwellstudio.co.uk
www.meadowlarkwellstudio.co.uk
appointments date and time & cancelation policy.
We require 24 hours cancellation for appointments otherwise a charge may be incurred.

```html
<!DOCTYPE html>
<html lang="en">
<head>
<meta charset="utf-8">
<title>Meadowlark Wellness Studio – Business Cards</title>
<link rel="stylesheet" href="https://fonts.googleapis.com/css2?family=Open+Sans:wght@400;600;700&family=Cinzel:wght@400&display=swap">
<style>
  :root {
    --stage: #e9ebe8;
    --paper: #ffffff;
    --ink: #4a4f52;
    --green-deep: #3f7d2c;
    --green-mid: #5e9a3c;
    --green-light: #7fb34f;
    --blue-deep: #0f5fa6;
    --blue-mid: #2d83cc;
    --blue-light: #5aa6e3;
    --name-green: #3e8a2f;
    --title-blue: #2d7fc1;
    --rule-grey: #d5d9dc;
  }
  * { box-sizing: border-box; margin: 0; padding: 0; }
  html, body { width: 1200px; height: 906px; overflow: hidden; }
  body { background: var(--stage); font-family: "Open Sans", Arial, sans-serif; position: relative; }

  .card {
    position: absolute;
    width: 405px;
    height: 226px;
    border-radius: 12px;
    box-shadow: 0 6px 18px rgba(0,0,0,0.25);
    overflow: hidden;
  }

  /* Front card */
  .card-front { left: 355px; top: 167px; background: var(--paper); }
  .card-front .brand {
    position: absolute; top: 22px; left: 0; width: 100%;
    text-align: center; display: flex; justify-content: center; align-items: center; gap: 8px;
  }
  .brand-dot { width: 12px; height: 12px; border-radius: 50%; background: var(--green-mid); }
  .brand-name {
    font-family: "Cinzel", Georgia, serif; font-size: 18px; color: var(--green-deep); letter-spacing: 0.5px;
  }
  .person { position: absolute; left: 22px; top: 110px; }
  .person-name { font-size: 15px; font-weight: 700; color: var(--name-green); }
  .person-title { font-size: 12px; font-weight: 600; color: var(--title-blue); text-align: center; }
  .contact { position: absolute; left: 182px; top: 102px; list-style: none; }
  .contact li { display: flex; align-items: center; gap: 6px; font-size: 8.5px; color: var(--ink); line-height: 12.5px; }
  .contact li.indent { padding-left: 16px; }
  .contact .icon { width: 10px; height: 10px; border-radius: 50%; background: var(--ink); flex: none; display: flex; align-items: center; justify-content: center; }
  .front-band { position: absolute; left: 0; bottom: 0; width: 100%; height: 30px; }

  /* Back cards */
  .card-back { color: #fff; text-align: center; }
  .card-green { left: 203px; top: 416px; background: linear-gradient(150deg, var(--green-light), var(--green-mid) 45%, var(--green-deep)); }
  .card-blue { left: 617px; top: 416px; background: linear-gradient(150deg, var(--blue-light), var(--blue-mid) 45%, var(--blue-deep)); }
  .card-back .brand {
    margin-top: 30px; display: flex; justify-content: center; align-items: center; gap: 8px;
  }
  .card-back .brand-dot { background: #fff; }
  .card-back .brand-name { color: #fff; font-size: 18px; }
  .policy-lead { margin-top: 26px; font-size: 12.5px; }
  .policy-note { margin-top: 18px; font-size: 12.5px; line-height: 18px; padding: 0 28px; }
</style>
</head>
<body>
  <section class="card card-front" aria-label="Business card front">
    <div class="brand"><span class="brand-dot"></span><span class="brand-name">Meadowlark Wellness Studio</span></div>
    <div class="person">
      <p class="person-name">Name Goes Here</p>
      <p class="person-title">Title</p>
    </div>
    <ul class="contact">
      <li><span class="icon"><svg width="6" height="7" viewBox="0 0 6 7"><path d="M3 0a2.5 2.5 0 0 0-2.5 2.5C.5 4.5 3 7 3 7s2.5-2.5 2.5-4.5A2.5 2.5 0 0 0 3 0z" fill="#fff"/></svg></span>12B Harlow Terrace</li>
      <li class="indent">Edinburgh</li>
      <li class="indent">EH4 7QN</li>
      <li><span class="icon"><svg width="6" height="6" viewBox="0 0 6 6"><path d="M1 0l1.2 1.6-.6.8a4 4 0 0 0 2 2l.8-.6L6 5 5 6C2 6 0 4 0 1z" fill="#fff"/></svg></span>0131 555 0192</li>
      <li><span class="icon"><svg width="6" height="5" viewBox="0 0 6 5"><rect x="0" y="0" width="6" height="5" fill="#fff"/><path d="M0 0l3 2.5L6 0" stroke="#4a4f52" stroke-width="0.8" fill="none"/></svg></span>info@meadowlarkwellstudio.co.uk</li>
      <li><span class="icon"><svg width="6" height="6" viewBox="0 0 6 6"><circle cx="3" cy="3" r="2.5" stroke="#fff" stroke-width="0.8" fill="none"/><path d="M0.5 3h5M3 0.5v5" stroke="#fff" stroke-width="0.6"/></svg></span>www.meadowlarkwellstudio.co.uk</li>
    </ul>
    <svg class="front-band" viewBox="0 0 405 30" preserveAspectRatio="none" aria-hidden="true">
      <path d="M0 12 Q200 0 405 8 L405 30 L0 30z" fill="var(--rule-grey)"/>
      <path d="M0 18 Q200 6 405 14 L405 30 L0 30z" fill="var(--green-mid)"/>
      <path d="M0 24 Q200 14 405 20 L405 30 L0 30z" fill="var(--blue-mid)"/>
    </svg>
  </section>

  <section class="card card-back card-green" aria-label="Business card back, green">
    <div class="brand"><span class="brand-dot"></span><span class="brand-name">Meadowlark Wellness Studio</span></div>
    <p class="policy-lead">appointments date and time &amp; cancelation policy.</p>
    <p class="policy-note">We require 24 hours cancellation for appointments otherwise a charge may be incurred.</p>
  </section>

  <section class="card card-back card-blue" aria-label="Business card back, blue">
    <div class="brand"><span class="brand-dot"></span><span class="brand-name">Meadowlark Wellness Studio</span></div>
    <p class="policy-lead">appointments date and time &amp; cancelation policy.</p>
    <p class="policy-note">We require 24 hours cancellation for appointments otherwise a charge may be incurred.</p>
  </section>
</body>
</html>
```